RW Business Card Design

My company provides advising/training and coaching services to business owners who want better financial results and better work/life balance. We help them through creating custom plans supported with education, strategic thinking and accountability.

We also help through some online courses which are geared to smaller businesses.
Updates

please also include our nth american contact # +1 555 208 4471

Industry/Entity Type

Financial

Contact Information for Business Card

Morgan Halberd
morgan@morganhalberd-example.com
+61 400 555 917
www.morganhalberd-example.com

```html
<!DOCTYPE html>
<html lang="en">
<head>
<meta charset="utf-8">
<title>RW Business Card</title>
<link href="https://fonts.googleapis.com/css2?family=Questrial&display=swap" rel="stylesheet">
<style>
  :root {
    --backdrop: #35373a;
    --navy-top: #0f5590;
    --navy-bottom: #07325e;
    --sky: #2b9fe0;
    --brand-blue: #1b62ad;
    --mist: #d6dde5;
    --paper: #f7f7f7;
    --paper-edge: #e6e6e6;
    --ink-grey: #777b80;
    --faint-mark: #dde5ee;
  }
  * { box-sizing: border-box; margin: 0; padding: 0; }
  html, body {
    width: 1200px; height: 1200px; overflow: hidden;
    background: var(--backdrop);
    font-family: "Questrial", "Century Gothic", sans-serif;
  }
  .canvas {
    width: 1200px; height: 1200px;
    display: flex; flex-direction: column; align-items: center; justify-content: center;
    gap: 60px;
  }
  .card {
    position: relative;
    width: 860px; height: 490px;
    border-radius: 38px;
    overflow: hidden;
    box-shadow: 0 18px 40px rgba(0,0,0,.45);
  }
  /* front */
  .card--front {
    background: linear-gradient(160deg, var(--navy-top) 0%, var(--navy-bottom) 100%);
  }
  .front-brand {
    position: absolute; left: 110px; top: 50%;
    transform: translateY(-50%);
    display: flex; align-items: center; gap: 34px;
  }
  .front-brand__dot {
    width: 120px; height: 120px; border-radius: 50%;
    background: var(--sky);
  }
  .front-brand__name {
    font-size: 50px; letter-spacing: 1px;
    color: var(--mist); text-transform: uppercase;
  }
  /* back */
  .card--back {
    background: linear-gradient(170deg, #ffffff 0%, var(--paper) 60%, var(--paper-edge) 100%);
  }
  .back-mark {
    position: absolute; left: 70px; top: 70px;
    width: 350px; height: 350px; border-radius: 50%;
    background: var(--faint-mark);
  }
  .contact {
    position: absolute; right: 60px; top: 90px;
    text-align: right;
  }
  .contact__name {
    font-size: 40px; color: var(--brand-blue);
    text-transform: uppercase; letter-spacing: .5px;
    margin-bottom: 26px;
  }
  .contact__row {
    display: flex; justify-content: flex-end; align-items: center; gap: 16px;
    font-size: 25px; color: var(--ink-grey);
    line-height: 1.55;
  }
  .contact__row--web { margin-top: 26px; }
  .contact__icon { width: 24px; height: 24px; flex: none; }
  .contact__icon--blank { visibility: hidden; }
  .contact__domain { color: var(--brand-blue); font-weight: 700; }
</style>
</head>
<body>
<main class="canvas">
  <section class="card card--front">
    <div class="front-brand">
      <span class="front-brand__dot"></span>
      <span class="front-brand__name">Morgan Halberd</span>
    </div>
  </section>

  <section class="card card--back">
    <div class="back-mark"></div>
    <div class="contact">
      <p class="contact__name">Morgan Halberd</p>
      <p class="contact__row">morgan@morganhalberd-example.com
        <svg class="contact__icon" viewBox="0 0 24 24"><rect x="2" y="5" width="20" height="14" rx="2" fill="var(--brand-blue)"/><path d="M3 6l9 7 9-7" fill="none" stroke="#fff" stroke-width="1.6"/></svg>
      </p>
      <p class="contact__row">+61 400 555 917
        <svg class="contact__icon" viewBox="0 0 24 24"><path d="M6.6 2.5l3 3.6-1.8 2.2c1.2 2.6 3.3 4.7 5.9 5.9l2.2-1.8 3.6 3-1.6 3.6C11 19 5 13 3 5.1z" fill="var(--brand-blue)"/></svg>
      </p>
      <p class="contact__row">+1 555 208 4471
        <svg class="contact__icon contact__icon--blank" viewBox="0 0 24 24"></svg>
      </p>
      <p class="contact__row contact__row--web">www.<span class="contact__domain">morganhalberd-example</span>.com
        <svg class="contact__icon" viewBox="0 0 24 24"><circle cx="12" cy="12" r="10" fill="var(--brand-blue)"/><g fill="none" stroke="#fff" stroke-width="1.3"><ellipse cx="12" cy="12" rx="4.5" ry="10"/><path d="M2 12h20M4 7h16M4 17h16"/></g></svg>
      </p>
    </div>
  </section>
</main>
</body>
</html>
```